Broschüre für Premium Kunstrasen
Zielgruppe
Hauptsächlich (70% unserer Tätigkeit) verlegen wir Premium Kunstrasen in Gärten von Privatleuten. Schlüsselfertig .
Unsere Auftraggeber in diesem Bereich sind in der Regel zwischen 35 bis 70 Jahre alt und gut situiert.
30% unserer Tätigkeit besteht aus der Lieferung von hochwertigen Kunstrasen für den Balkon, Terrasse.
Unsere Produkte haben lange Garantiezeiten von 15 Jahren. Deshalb nennen wir unsere Produkte auch Sonnhalm
Aufgabenstellung
Textvorgaben und Headlines kommen von uns

```html
<!DOCTYPE html>
<html lang="de">
<head>
<meta charset="utf-8">
<title>Kunstrasen Grünfeld – Broschüre</title>
<link rel="stylesheet" href="https://fonts.googleapis.com/css2?family=Oswald:wght@600;700&family=Montserrat:wght@400;600;700&display=swap">
<style>
  :root {
    --green-dark: #1d5a22;
    --green-mid: #2f6f2a;
    --green-light: #7bb33a;
    --olive: #a18d2c;
    --olive-dark: #8a7824;
    --white: #ffffff;
    --paper: #f3f3f1;
    --ink: #2b2b2b;
    --backdrop: #dcdcdc;
  }
  * { box-sizing: border-box; margin: 0; padding: 0; }
  html, body { width: 838px; height: 1200px; overflow: hidden; }
  body { background: var(--backdrop); font-family: "Montserrat", sans-serif; color: var(--ink); position: relative; }
  .spread { position: absolute; left: 0; width: 838px; height: 585px; overflow: hidden; background: var(--white); box-shadow: 0 2px 8px rgba(0,0,0,.25); }
  .spread-outer { top: 10px; }
  .spread-inner { top: 605px; }
  .page { position: absolute; top: 0; width: 419px; height: 585px; overflow: hidden; }
  .page-left { left: 0; }
  .page-right { left: 419px; }
  .abs { position: absolute; }
  .shape { position: absolute; left: 0; top: 0; }
  .photo { position: absolute; }

  /* back cover */
  .portrait { left: 122px; top: 94px; width: 176px; height: 176px; border-radius: 50%; border: 6px solid var(--white);
    background: radial-gradient(circle at 50% 45%, #c9a58a 0 30%, #6a7d5a 60%, #3e5a34 100%); }
  .contact-name { left: 0; width: 419px; top: 284px; text-align: center; color: var(--white); font-weight: 600; font-size: 14px; }
  .contact-bar { left: 78px; top: 308px; width: 262px; height: 26px; border-radius: 13px; background: var(--green-dark); color: var(--white);
    font-weight: 700; font-size: 16px; text-align: center; line-height: 26px; }
  .contact-phone { left: 78px; top: 340px; color: var(--white); font-weight: 700; font-size: 27px; display: flex; align-items: center; gap: 6px; }
  .contact-line { left: 86px; color: var(--white); font-weight: 700; font-size: 13px; display: flex; align-items: center; gap: 6px; }
  .contact-web { top: 381px; }
  .contact-mail { top: 402px; }
  .dot { width: 9px; height: 9px; border-radius: 50%; background: var(--white); opacity: .8; }
  .quote-title { left: 200px; top: 476px; color: var(--olive); font-weight: 700; font-size: 22px; }
  .quote-text { left: 40px; top: 508px; width: 330px; color: var(--white); font-size: 9px; line-height: 1.3; padding-left: 24px; }
  .quote-mark { position: absolute; font-family: Georgia, serif; font-size: 30px; line-height: 1; color: var(--white); font-weight: 700; }
  .quote-author { left: 64px; top: 552px; color: var(--green-light); font-size: 9px; font-weight: 700; }

  /* front cover */
  .brand { left: 0; width: 419px; top: 58px; display: flex; align-items: center; justify-content: center; gap: 10px; color: var(--white);
    font-weight: 700; font-size: 30px; }
  .brand-mark { width: 18px; height: 18px; border-radius: 50%; background: var(--green-light); }
  .cover-title { left: 0; width: 419px; top: 428px; text-align: center; font-family: "Oswald", sans-serif; font-weight: 700; font-size: 40px;
    color: var(--green-dark); line-height: 1; }
  .cover-sub { left: 0; width: 419px; top: 478px; text-align: center; font-weight: 600; font-size: 19px; line-height: 1.1; color: #111; }
  .cover-url { left: 80px; top: 553px; width: 256px; height: 32px; background: var(--green-dark); color: var(--white); font-weight: 700;
    font-size: 15px; text-align: center; line-height: 32px; }

  /* inner */
  .intro-title { left: 40px; top: 34px; font-family: "Oswald", sans-serif; font-weight: 600; font-size: 22px; color: var(--green-dark);
    border-left: 3px solid var(--olive); padding-left: 8px; line-height: 1.1; }
  .intro-text { left: 52px; width: 340px; font-size: 10px; line-height: 1.35; }
  .intro-a { top: 72px; }
  .intro-b { top: 120px; }
  .section-bar { height: 28px; border-radius: 14px; background: var(--olive); color: var(--white); font-weight: 700; font-size: 17px;
    text-align: center; line-height: 28px; }
  .bar-kunstrasen { left: 44px; top: 174px; width: 328px; }
  .bar-verlegen { left: 46px; top: 51px; width: 328px; }
  .item-photo { border: 3px solid var(--white); }
  .item-title { font-weight: 700; font-size: 14px; color: var(--white); line-height: 1.1; }
  .item-text { font-size: 10px; line-height: 1.3; color: var(--white); }
  .verlegen-title { color: var(--green-dark); font-weight: 700; font-size: 15px; line-height: 1.05; }
  .verlegen-text { font-size: 9.5px; line-height: 1.3; color: var(--ink); }
  .verlegen-photo { border: 3px solid var(--green-light); }
  .feature { width: 120px; text-align: center; }
  .feature-circle { width: 88px; height: 88px; border-radius: 50%; background: var(--green-dark); border: 4px solid var(--white); margin: 0 auto;
    display: flex; align-items: center; justify-content: center; }
  .feature-label { margin-top: 8px; color: var(--white); font-weight: 700; font-size: 11px; line-height: 1.15; }
</style>
</head>
<body>

<!-- Außenseite: Rückseite + Titel -->
<section class="spread spread-outer">
  <div class="page page-left">
    <div class="photo" style="left:0;top:0;width:419px;height:220px;background:linear-gradient(160deg,#e9ecef 0%,#b7bcc1 45%,#5c8a3a 80%,#3d6b2a 100%);" role="img" aria-label="Foto: Dachterrasse mit Kunstrasen, Lounge-Möbeln und Topfpflanzen"></div>
    <svg class="shape" width="419" height="585" viewBox="0 0 419 585" aria-hidden="true">
      <polygon points="0,210 419,178 419,440 0,470" fill="var(--olive)"/>
      <polygon points="0,470 419,432 419,445 0,482" fill="var(--white)"/>
      <polygon points="0,482 419,445 419,585 0,585" fill="var(--green-dark)"/>
      <polygon points="0,200 419,168 419,178 0,210" fill="var(--green-dark)"/>
    </svg>
    <div class="abs portrait" role="img" aria-label="Porträtfoto des Ansprechpartners"></div>
    <p class="abs contact-name">Jonas Berger</p>
    <p class="abs contact-bar">Contact Us</p>
    <p class="abs contact-phone">
      <svg width="24" height="24" viewBox="0 0 24 24" aria-hidden="true"><circle cx="12" cy="12" r="12" fill="#fff"/><path d="M8.5 6.5l2 2-1.2 1.6c.8 1.6 2 2.8 3.6 3.6l1.6-1.2 2 2-1.4 1.7c-3.8-.6-7.3-4.1-7.9-7.9z" fill="var(--olive)"/></svg>
      0151 23468097
    </p>
    <p class="abs contact-line contact-web"><span class="dot"></span>www.kunstrasen-gruenfeld.de</p>
    <p class="abs contact-line contact-mail"><span class="dot"></span>info@kunstrasen-gruenfeld.de</p>
    <h3 class="abs quote-title">Kundenzitat</h3>
    <p class="abs quote-text"><span class="quote-mark" style="left:0;top:-2px;">“</span>Ihr Team kennt sich perfekt mit der Verlegung von Kunstrasen aus. Unsere Wünsche wurden berücksichtigt &amp; wir sind sehr zufrieden mit der Umsetzung.<span class="quote-mark" style="right:-4px;bottom:-16px;">”</span></p>
    <p class="abs quote-author">– Familie K. aus Lindenfeld</p>
  </div>

  <div class="page page-right">
    <div class="photo" style="left:0;top:120px;width:419px;height:300px;background:linear-gradient(170deg,#dfe6ea 0%,#8fae74 40%,#3f8a2c 75%,#5ea03a 100%);" role="img" aria-label="Foto: Garten mit gepflegtem Kunstrasen, Sträuchern und Terrassenplatten"></div>
    <svg class="shape" width="419" height="585" viewBox="0 0 419 585" aria-hidden="true">
      <path d="M0,0 H419 V112 Q210,160 0,128 Z" fill="var(--green-dark)"/>
      <polygon points="330,150 419,118 419,210" fill="var(--olive)"/>
      <path d="M0,390 Q180,440 419,380 V585 H0 Z" fill="var(--white)"/>
      <polygon points="300,398 419,330 419,386" fill="var(--olive)"/>
      <rect x="0" y="528" width="419" height="57" fill="url(#grassFade)"/>
      <defs>
        <linearGradient id="grassFade" x1="0" y1="0" x2="0" y2="1">
          <stop offset="0" stop-color="#8cc640" stop-opacity="0"/>
          <stop offset="1" stop-color="#4e9a2a"/>
        </linearGradient>
      </defs>
    </svg>
    <p class="abs brand"><span class="brand-mark"></span>Kunstrasen Grünfeld</p>
    <h1 class="abs cover-title">Kunstrasen Grünfeld</h1>
    <p class="abs cover-sub">Kunstrasen für Garten,<br>Balkon &amp; Terrasse</p>
    <p class="abs cover-url">www.kunstrasen-gruenfeld.de</p>
  </div>
</section>

<!-- Innenseite -->
<section class="spread spread-inner">
  <div class="page page-left">
    <svg class="shape" width="419" height="585" viewBox="0 0 419 585" aria-hidden="true">
      <rect width="419" height="585" fill="var(--paper)"/>
      <path d="M0,165 Q200,180 419,150 V585 H0 Z" fill="var(--green-dark)"/>
    </svg>
    <h2 class="abs intro-title">Partner für Premium Kunstrasen</h2>
    <p class="abs intro-text intro-a">Premium Kunstrasen sind unsere Leidenschaft. Wir begleiten Sie von der Idee, über die Planung und Sortenwahl bis hin zur schlüsselfertigen Verlegung.</p>
    <p class="abs intro-text intro-b">Haben Sie Fragen oder benötigen Sie Informationen?<br>Rufen Sie einfach an oder schreiben Sie mir.</p>
    <p class="abs section-bar bar-kunstrasen">Kunstrasen</p>

    <div class="photo item-photo" style="left:41px;top:232px;width:134px;height:94px;background:linear-gradient(160deg,#cfd6d9,#7c8c6a 50%,#4d8a30);" role="img" aria-label="Foto: Garten mit Kunstrasenfläche"></div>
    <h3 class="abs item-title" style="left:195px;top:236px;">Kunstrasen Garten</h3>
    <p class="abs item-text" style="left:195px;top:256px;width:205px;">Lassen Sie die mühselige Rasenpflege der Vergangenheit angehören. Mit unserem Premium Kunstrasen können Sie sich im Garten entspannen.</p>

    <div class="photo item-photo" style="left:41px;top:348px;width:134px;height:94px;background:linear-gradient(160deg,#9aa0a4,#6b6257 50%,#3f3a34);" role="img" aria-label="Foto: Balkon mit Kunstrasen und Sitzmöbeln"></div>
    <h3 class="abs item-title" style="left:195px;top:352px;">Kunstrasen Balkon</h3>
    <p class="abs item-text" style="left:195px;top:372px;width:205px;">Zaubern Sie auf Ihrem Balkon wohnliche und pflegeleichte Flächen z.B. auf Holz, Beton oder Fliesen – mit unseren hochwertigen und langelebigen Kunstrasen.</p>

    <div class="photo item-photo" style="left:41px;top:464px;width:134px;height:94px;background:linear-gradient(170deg,#8a8d90,#5a5f60 45%,#4f9a2e);" role="img" aria-label="Foto: Terrasse mit Kunstrasenfläche"></div>
    <h3 class="abs item-title" style="left:195px;top:468px;">Kunstrasen Terrasse</h3>
    <p class="abs item-text" style="left:195px;top:488px;width:205px;">Sie möchten Ihre Terrasse oder Dachterrasse ein wenig freundlicher gestalten? Mit unseren Kunstrasen verwandeln Sie Ihre Terrasse in eine grüne Oase.</p>
  </div>

  <div class="page page-right">
    <div class="photo" style="left:0;top:0;width:419px;height:60px;background:linear-gradient(180deg,#6a9a45,#3f7a2a);" role="img" aria-label="Foto: Kunstrasenfläche mit Kies"></div>
    <svg class="shape" width="419" height="585" viewBox="0 0 419 585" aria-hidden="true">
      <path d="M0,30 Q200,50 419,40 V585 H0 Z" fill="var(--paper)"/>
      <path d="M0,400 Q200,410 419,380 V585 H0 Z" fill="var(--olive)"/>
      <path d="M0,400 Q200,410 419,380 V396 Q200,424 0,418 Z" fill="var(--green-light)" opacity=".6"/>
    </svg>
    <p class="abs section-bar bar-verlegen">Verlegen</p>

    <div class="photo verlegen-photo" style="left:43px;top:101px;width:130px;height:116px;background:linear-gradient(170deg,#b9d3ea,#cfd8dc 45%,#4f8f34 75%);" role="img" aria-label="Foto: Verlegung von Kunstrasen vor einem Pavillon"></div>
    <h3 class="abs verlegen-title" style="left:190px;top:104px;width:210px;">Kunstrasen verlegen lassen</h3>
    <p class="abs verlegen-text" style="left:190px;top:138px;width:212px;">Ihnen fehlt Zeit und Muße Kunstrasen selber zu installieren? Sie möchten Kunstrasen von einem Experten fachmännisch verlegen lassen? Wir kümmern uns um Ihr Kunstrasen-Projekt. Angefangen bei der individuellen Beratung über die Planung bis hin zur Umsetzung.</p>

    <div class="photo verlegen-photo" style="left:43px;top:263px;width:130px;height:116px;background:linear-gradient(175deg,#a9c6e6,#7a9a5a 40%,#6b5a48 75%);" role="img" aria-label="Foto: vorbereitete Fläche im Garten vor der Verlegung"></div>
    <h3 class="abs verlegen-title" style="left:190px;top:266px;width:210px;">Kunstrasen selbst verlegen</h3>
    <p class="abs verlegen-text" style="left:190px;top:300px;width:212px;">Wenn Sie unsere Kunstrasen selbst verlegen möchten, verraten wir Ihnen, auf was es ankommt und geben Ihnen Schritt für Schritt Hilfestellung – damit Ihr Kunstrasen perfekt verlegt werden kann.</p>

    <div class="abs feature" style="left:35px;top:404px;">
      <div class="feature-circle">
        <svg width="46" height="30" viewBox="0 0 46 30" aria-hidden="true"><path d="M12 4 L2 15 L12 26" stroke="#fff" stroke-width="5" fill="none" stroke-linejoin="round"/><path d="M34 4 L44 15 L34 26" stroke="var(--green-light)" stroke-width="5" fill="none" stroke-linejoin="round"/><path d="M26 2 L20 28" stroke="var(--green-light)" stroke-width="4"/></svg>
      </div>
      <p class="feature-label">Alles aus einer Hand – Verlegung bundesweit</p>
    </div>
    <div class="abs feature" style="left:149px;top:404px;">
      <div class="feature-circle">
        <svg width="36" height="42" viewBox="0 0 36 42" aria-hidden="true"><path d="M10 24 L5 40 L12 36 L15 42 L18 28 Z M26 24 L31 40 L24 36 L21 42 L18 28 Z" fill="#fff"/><circle cx="18" cy="15" r="14" fill="var(--green-light)"/><circle cx="18" cy="15" r="8" fill="none" stroke="#fff" stroke-width="2.5"/></svg>
      </div>
      <p class="feature-label">Individuelle Beratung und erstklassiger Kunstrasen</p>
    </div>
    <div class="abs feature" style="left:263px;top:404px;">
      <div class="feature-circle">
        <svg width="42" height="42" viewBox="0 0 42 42" aria-hidden="true"><rect x="2" y="20" width="18" height="18" fill="#fff"/><rect x="22" y="4" width="18" height="18" fill="var(--green-light)"/><rect x="22" y="24" width="14" height="14" fill="var(--green-light)" opacity=".7"/><rect x="4" y="6" width="14" height="12" fill="#fff" opacity=".7"/></svg>
      </div>
      <p class="feature-label">Qualifizierung &amp; Lösungen für Ihr Kunstrasen Projekt</p>
    </div>
  </div>
</section>

</body>
</html>
```